DeskWizard.dk Frontpage design

I'm in the process of starting a It-course website, based in Denmark. The web site Url is - www.deskwizard.dk

The services are:
- Online courses (This is the main service and the most important)
- One to One courses
- Webinar

I need a frontpage design a simple design, but it must shows professionalism. I have no preference in color, but I like white space.

In Denmark the established competitors are:
- www.tasniva.dk (Biggest competitor)
- www.bramfeldt.dk/online-kurser
- www.velunda.dk

Target Market(s)

Mainly companies (B to B), but there are also a small number of private customers

Industry/Entity Type

Online it courses and one to one consulting

Number of Pages Required

1 page

Font styles to use
Sans Serif

Requirements
Must have
• A professional design, white space

```html
<!DOCTYPE html>
<html lang="en">
<head>
<meta charset="utf-8">
<title>DeskWizard.dk – Online IT courses and one to one consulting</title>
<link rel="stylesheet" href="https://fonts.googleapis.com/css2?family=Poppins:wght@400;500;600;700&display=swap">
<style>
:root{
  --green:#16b157;
  --green-dark:#0f9a4a;
  --green-light:#a5d57f;
  --ink:#16181f;
  --text:#5d6069;
  --muted:#9a9da5;
  --panel:#f4f4f5;
  --band:#eeeeef;
  --footer:#1b2230;
  --footer-text:#c3c7d0;
  --star:#f5b400;
  --photo-warm:linear-gradient(135deg,#d9b28f,#7a5a46);
  --photo-cool:linear-gradient(135deg,#c7ccd3,#5f6670);
}
*{box-sizing:border-box;margin:0;padding:0}
html,body{width:1200px;height:4789px;overflow:hidden}
body{position:relative;background:#fff;font-family:"Poppins",sans-serif;color:var(--ink)}
.abs{position:absolute}
.btn{position:absolute;display:flex;align-items:center;justify-content:center;background:var(--green);color:#fff;font-size:11px;font-weight:600;border-radius:24px;text-transform:uppercase;letter-spacing:.2px}
.photo{position:absolute;overflow:hidden}
.round{border-radius:50%}

/* header */
.logo{left:88px;top:28px;font-size:32px;font-weight:600;color:var(--green);letter-spacing:-.5px}
.logo b{color:var(--ink);font-weight:600}
.nav{left:366px;top:42px;display:flex;gap:36px;font-size:12.5px;font-weight:500}
.try{left:980px;top:30px;width:130px;height:40px;border:2px solid #dcdcdc;border-radius:22px;display:flex;align-items:center;justify-content:center;font-size:11.5px;font-weight:600}

/* hero */
.hero-title{left:88px;top:262px;font-size:56px;line-height:59px;font-weight:700;letter-spacing:-1px}
.hero-text{left:88px;top:462px;width:400px;font-size:14px;line-height:24px;color:var(--text)}
.tablet{left:684px;top:262px;width:428px;height:330px;background:#1d1f25;border-radius:20px;padding:12px}
.screen{width:100%;height:100%;background:#f5f6fa;border-radius:10px;position:relative;overflow:hidden;font-size:6px;color:var(--muted)}

.ghost{left:0;top:682px;font-size:128px;font-weight:700;color:#f0f0f1;letter-spacing:-2px}
.feature-box{left:88px;top:800px;width:1024px;height:305px;background:var(--panel);border-radius:40px}
.feature-head{left:0;width:1200px;top:866px;text-align:center;font-size:17px;font-weight:600}
.fcard{top:920px;width:230px;height:260px;background:#fff;border-radius:8px;box-shadow:0 10px 30px rgba(0,0,0,.06);text-align:center;padding-top:30px}
.fcard h3{font-size:13.5px;font-weight:600;line-height:20px;margin-top:18px}
.fcard p{font-size:11.5px;line-height:19px;color:var(--text);margin:18px 18px 0}

.h2{font-size:32px;line-height:40px;font-weight:700;letter-spacing:-.5px}
.para{font-size:14px;line-height:22px;color:var(--text)}

/* meeting mockup */
.meet{left:95px;top:1303px;width:560px;height:352px;background:#fff;border:3px solid #1d1f25;border-radius:14px;overflow:hidden;box-shadow:0 20px 40px rgba(0,0,0,.08)}
.tag{position:absolute;height:16px;padding:0 10px;border-radius:8px;background:var(--green-light);color:#fff;font-size:7px;font-weight:600;display:flex;align-items:center}

/* services */
.band{left:0;top:2150px;width:1200px;height:510px;background:var(--band)}
.scard{top:1838px;width:246px;height:365px;background:#fff;border-radius:6px;overflow:hidden;box-shadow:0 10px 30px rgba(0,0,0,.06)}
.scard .img{height:205px}
.scard .body{border-left:3px solid var(--green);margin:20px 0 0 0;padding-left:22px}
.scard h3{font-size:15px;font-weight:600}
.scard p{font-size:11.5px;line-height:19px;color:var(--text);margin-top:8px;padding-right:16px}
.scard a{display:block;margin:18px 0 0 25px;font-size:10.5px;font-weight:600;color:var(--muted);text-decoration:underline}

.ecard{top:2818px;width:249px;height:219px;border-radius:4px}
.ecard .play{position:absolute;left:50%;top:50%;width:34px;height:34px;margin:-17px;border-radius:50%;background:rgba(0,0,0,.25)}
.arrow{width:36px;height:36px;border-radius:50%;background:#f1f1f2;display:flex;align-items:center;justify-content:center}

/* testimonials */
.tcard{top:3800px;width:326px;height:218px;background:#fff;border-radius:8px;box-shadow:0 10px 30px rgba(0,0,0,.07);padding:72px 24px 0}
.tcard p{font-size:12.5px;line-height:22px;color:var(--text)}
.tcard .name{position:absolute;left:24px;top:166px;font-size:13px;font-weight:600}
.tcard .stars{position:absolute;right:24px;top:166px;color:var(--star);font-size:12px;letter-spacing:1px}
.tcard .quote{position:absolute;right:30px;top:28px;font-size:80px;line-height:60px;color:#ececee;font-weight:700}
.avatar{top:3763px;width:74px;height:74px;border-radius:50%;border:4px solid #fff}
.partner{top:4093px;width:150px;height:150px;border-radius:50%;background:#f3f3f4;display:flex;align-items:center;justify-content:center;gap:8px;font-size:15px;font-weight:600;color:#4a4d55}
.partner i{display:block;width:14px;height:14px;border-radius:50%;background:#4a4d55}

/* footer */
.footer{left:0;top:4346px;width:1200px;height:443px;background:var(--footer);color:var(--footer-text)}
.fcol{position:absolute;top:86px}
.fcol h4{color:#fff;font-size:19px;font-weight:600;margin-bottom:24px}
.fcol li{list-style:none;font-size:12.5px;line-height:27px}
.contact{font-size:12px;line-height:18px;margin-bottom:20px;padding-left:20px;position:relative}
.contact b{color:#fff;font-weight:500;font-size:11px;display:block}
.contact svg{position:absolute;left:0;top:2px}
.social{top:4522px;width:36px;height:36px;border-radius:50%;border:1px solid #3a4252;display:flex;align-items:center;justify-content:center}
.social i{width:10px;height:10px;border-radius:2px;background:#fff}
</style>
</head>
<body>

<!-- header -->
<div class="abs logo">desk<b>wizard</b></div>
<nav class="abs nav"><span>ONLINE COURSES</span><span>COMPANY AGREEMENT</span><span>RESOURCES</span><span>ABOUT US</span><span>SIGN IN</span></nav>
<div class="abs try">TRY FOR FREE</div>

<!-- hero -->
<svg class="abs" style="left:780px;top:110px" width="420" height="650" viewBox="0 0 420 650">
  <path d="M56 10 A160 160 0 0 1 56 330 Z" fill="#58a63f"/>
  <circle cx="390" cy="80" r="72" fill="#c3e19c"/>
  <path d="M20 440 L166 440 L166 620 A146 146 0 0 1 20 474 Z" fill="#6fb24b"/>
  <path d="M-38 620 A47 47 0 0 1 56 620 Z" fill="var(--green)"/>
</svg>
<div class="abs hero-title">Online it courses<br>and one to one<br>consulting</div>
<p class="abs hero-text">Train your employees online exactly when it fits into a busy day. They do not have to leave the office...</p>
<div class="btn" style="left:88px;top:535px;width:167px;height:46px">See our courses</div>

<div class="photo round" role="img" aria-label="Portrait of a smiling man in a blue shirt" style="left:705px;top:130px;width:130px;height:130px;background:var(--photo-cool)"></div>
<div class="photo round" role="img" aria-label="Woman in a green sweater and hat talking on a phone" style="left:548px;top:335px;width:180px;height:180px;background:linear-gradient(135deg,#7fb0c6,#3d7a3a)"></div>
<div class="photo round" role="img" aria-label="Woman with red hair looking at a phone" style="left:1110px;top:425px;width:110px;height:110px;background:linear-gradient(135deg,#e9d3c4,#c0523e)"></div>
<div class="photo round" role="img" aria-label="Woman with glasses smiling at a laptop" style="left:950px;top:585px;width:150px;height:150px;background:var(--photo-warm)"></div>

<div class="abs tablet"><div class="screen">
  <div class="abs" style="left:0;top:0;width:60px;height:306px;background:#fff"></div>
  <div class="abs" style="left:8px;top:28px;width:42px;height:10px;border-radius:3px;background:#1d1f25"></div>
  <div class="abs" style="left:8px;top:48px;width:40px;height:4px;background:#e4e5ea"></div>
  <div class="abs" style="left:8px;top:60px;width:36px;height:4px;background:#e4e5ea"></div>
  <div class="abs" style="left:8px;top:72px;width:40px;height:4px;background:#e4e5ea"></div>
  <div class="abs" style="left:8px;top:84px;width:32px;height:4px;background:#e4e5ea"></div>
  <div class="photo" role="img" aria-label="Video call with a smiling woman" style="left:72px;top:82px;width:150px;height:100px;border-radius:6px;background:linear-gradient(135deg,#f2ece6,#8b5a3f)"></div>
  <div class="abs" style="left:72px;top:192px;color:#1d1f25;font-weight:600">Team Talk</div>
  <div class="abs" style="left:72px;top:204px;width:150px;height:58px;background:#fff;border-radius:6px"></div>
  <div class="abs" style="left:240px;top:84px;width:130px;height:110px;background:#fff;border-radius:6px"></div>
  <div class="abs" style="left:240px;top:204px;color:#1d1f25;font-weight:600">Reminder</div>
  <div class="abs" style="left:240px;top:216px;width:120px;height:14px;border-radius:3px;background:#f3d57a"></div>
  <div class="abs" style="left:240px;top:236px;width:120px;height:14px;border-radius:3px;background:#f3d57a"></div>
</div></div>

<!-- features -->
<div class="abs ghost">Courses</div>
<div class="abs feature-box"></div>
<div class="abs feature-head">Online IT Courses and One to One Consulting</div>
<div class="abs fcard" style="left:237px">
  <svg width="56" height="56" viewBox="0 0 56 56" fill="none" stroke="var(--green)" stroke-width="2.4"><circle cx="28" cy="30" r="22"/><path d="M28 18v12l8 6M20 5l-8 6M36 5l8 6"/></svg>
  <h3>Get rid of the<br>employee</h3>
  <p>Full compliment of services which provide the entire claim process in your service...</p>
</div>
<div class="abs fcard" style="left:486px">
  <svg width="56" height="56" viewBox="0 0 56 56" fill="none" stroke="var(--green)" stroke-width="2.4"><path d="M28 6c-8 0-12 4-13 9-6 1-9 6-8 11-3 3-3 9 1 12 0 6 5 10 11 10 3 4 6 4 9 2z"/><path d="M28 6c8 0 12 4 13 9 6 1 9 6 8 11 3 3 3 9-1 12 0 6-5 10-11 10-3 4-6 4-9 2z"/><path d="M28 6v44M18 20h6M32 26h8M16 34h8M32 38h6"/></svg>
  <h3>Create far more<br>effective learning</h3>
  <p>Full compliment of services which provide the entire claim process in your service...</p>
</div>
<div class="abs fcard" style="left:734px">
  <svg width="72" height="56" viewBox="0 0 72 56" fill="none" stroke="var(--green)" stroke-width="2.4"><circle cx="44" cy="28" r="22"/><path d="M50 19c-2-3-11-3-11 2s12 3 12 9-10 6-13 2M44 13v4M44 40v4M4 18h12M0 28h14M6 38h12"/></svg>
  <h3>Much cheaper than<br>physical courses</h3>
  <p>Full compliment of services which provide the entire claim process in your service...</p>
</div>

<!-- just-in-time -->
<div class="abs" style="left:-60px;top:1420px;width:320px;height:300px;border-radius:50%;background:radial-gradient(circle at 70% 30%,#d8ecec,#fff 70%)"></div>
<div class="abs round" style="left:605px;top:1278px;width:100px;height:100px;background:#f1f1f2"></div>
<div class="abs meet">
  <div class="abs" style="left:14px;top:12px;width:16px;height:16px;border-radius:3px;background:var(--green)"></div>
  <div class="abs" style="left:38px;top:14px;font-size:10px;font-weight:600">Meetly</div>
  <div class="abs" style="left:88px;top:10px;font-size:8px;font-weight:600">UX/UI Design Conference Meeting</div>
  <div class="abs" style="left:88px;top:21px;font-size:7px;color:var(--muted)">Productivity</div>
  <div class="photo" role="img" aria-label="Video call with a woman wearing glasses" style="left:14px;top:50px;width:310px;height:230px;border-radius:8px;background:linear-gradient(135deg,#ece4dc,#a07456)"></div>
  <div class="photo" role="img" aria-label="Participant thumbnails" style="left:330px;top:56px;width:48px;height:220px;border-radius:6px;background:linear-gradient(180deg,#e58a8a,#f0a54a,#4bb7c4)"></div>
  <div class="abs" style="left:14px;top:290px;width:370px;height:46px;border-radius:6px;background:#f5f6f8"></div>
  <div class="abs" style="left:398px;top:16px;font-size:8px;font-weight:600">Chat with Mia</div>
  <div class="abs" style="left:398px;top:48px;width:128px;height:62px;border-radius:6px;background:var(--green);color:#fff;font-size:7px;padding:8px">Current Plan<br><br>Monthly</div>
  <div class="abs" style="left:398px;top:122px;width:128px;height:150px;border-radius:6px;background:#f7f7f9"></div>
  <div class="abs" style="left:398px;top:300px;width:128px;height:22px;border-radius:11px;background:#f3f3f5"></div>
</div>
<div class="tag" style="left:62px;top:1522px">LEAD MARKETING</div>
<div class="tag" style="left:618px;top:1585px">PRODUCT MANAGER</div>
<div class="tag" style="left:426px;top:1685px">UX DESIGNER</div>

<div class="abs h2" style="left:770px;top:1312px;width:400px">Strengthen your<br>continuing education<br>with just-in-time<br>learning</div>
<p class="abs para" style="left:770px;top:1487px;width:330px">Aenean sollicitudin lorem quis bibendum auctor nisi elit consequat ipsum nec sagittis sem nibh id elit duis sed odio sit amet nibh vulputate cursus...</p>
<div class="btn" style="left:770px;top:1596px;width:166px;height:46px">See our courses</div>

<!-- services -->
<div class="abs band"></div>
<div class="abs h2" style="left:0;width:1200px;top:1773px;text-align:center">Our services</div>
<div class="abs scard" style="left:219px"><div class="img" role="img" aria-label="Woman with headphones studying at a laptop" style="background:linear-gradient(135deg,#f1d9a5,#e09a2c)"></div><div class="body"><h3>Online courses</h3><p>Full compliment of services which provide the entire claim process in your service...</p></div><a>READ MORE</a></div>
<div class="abs scard" style="left:478px"><div class="img" role="img" aria-label="Man working at a laptop in a café" style="background:linear-gradient(135deg,#e6d27a,#9a7447)"></div><div class="body"><h3>One to One courses</h3><p>Full compliment of services which provide the entire claim process in your service...</p></div><a>READ MORE</a></div>
<div class="abs scard" style="left:738px"><div class="img" role="img" aria-label="Laptop showing a group video call" style="background:var(--photo-cool)"></div><div class="body"><h3>Webinar</h3><p>Full compliment of services which provide the entire claim process in your service...</p></div><a>READ MORE</a></div>

<!-- teachers -->
<div class="abs" style="left:185px;top:2338px;font-size:13px">Meet The Teachers</div>
<div class="abs h2" style="left:185px;top:2362px">Denmark's leading<br>experts</div>
<p class="abs para" style="left:185px;top:2456px;width:320px">Aenean sollicitudin lorem quis bibendum auctor nisi elit consequat ipsum nec sagittis sem nibh id elit duis sed odio sit amet nibh vulputate cursus...</p>
<div class="photo round" role="img" aria-label="Group of smiling young people looking down at the camera" style="left:585px;top:2285px;width:430px;height:430px;background:linear-gradient(135deg,#a9b7c2,#6b5444)"></div>
<div class="abs round" style="left:573px;top:2593px;width:94px;height:94px;background:var(--green);display:flex;align-items:center;justify-content:center"><svg width="22" height="24"><path d="M4 2l16 10-16 10z" fill="#fff"/></svg></div>

<!-- examples -->
<div class="photo ecard" role="img" aria-label="Woman working on a laptop at a desk" style="left:88px;background:var(--photo-warm)"><span class="play"></span></div>
<div class="photo ecard" role="img" aria-label="Smiling man in a tan jacket" style="left:344px;background:linear-gradient(135deg,#c9a27b,#5b4033)"><span class="play"></span></div>
<div class="photo ecard" role="img" aria-label="Woman with braids studying with notes" style="left:602px;background:linear-gradient(135deg,#d4d7de,#4a4f5a)"><span class="play"></span></div>
<div class="abs h2" style="left:920px;top:2826px">Examples of<br>E-learning</div>
<p class="abs" style="left:920px;top:2928px;font-size:13px;line-height:21px;color:var(--text)">Which you have never<br>experienced it before</p>
<div class="abs arrow" style="left:922px;top:2991px"><svg width="8" height="10"><path d="M6 1L2 5l4 4" stroke="#333" fill="none" stroke-width="1.6"/></svg></div>
<div class="abs arrow" style="left:968px;top:2991px"><svg width="8" height="10"><path d="M2 1l4 4-4 4" stroke="#333" fill="none" stroke-width="1.6"/></svg></div>

<!-- get started -->
<div class="photo round" role="img" aria-label="Top view of people sitting in a circle with laptops" style="left:175px;top:3120px;width:470px;height:440px;background:radial-gradient(circle,#fff 48%,#e8ecf2 49%,#e8ecf2 70%,#fff 71%)"></div>
<div class="abs" style="left:705px;top:3212px;font-size:32px;font-weight:600;letter-spacing:-.5px">Get started easily</div>
<div class="abs" style="left:705px;top:3266px;font-size:13.5px;font-weight:500">Without having to involve your IT department</div>
<p class="abs para" style="left:705px;top:3305px;width:320px">Aenean sollicitudin lorem quis bibendum auctor nisi elit consequat ipsum nec sagittis sem nibh id elit duis sed odio sit amet nibh vulputate cursus...</p>
<div class="btn" style="left:705px;top:3413px;width:246px;height:46px">Read more about businesses</div>

<div class="abs" style="left:88px;top:3613px;width:1024px;height:1px;background:#e3e3e5"></div>

<!-- testimonials -->
<div class="abs" style="left:0;width:1200px;top:3665px;text-align:center;font-size:31px;font-weight:600">What our client say about us</div>
<div class="abs" style="left:0;width:1200px;top:3714px;text-align:center;font-size:15px;color:var(--text)">We're Trusted by over 6,000 customers</div>
<div class="abs tcard" style="left:90px"><span class="quote">“</span><p>"Very professional, courteous and fast. Nordvik seems to have solved all of our issues that we've been experiencing."</p><span class="name">Lars Holmberg</span><span class="stars">★★★★★</span></div>
<div class="abs tcard" style="left:437px"><span class="quote">“</span><p>"Very professional, courteous and fast. Nordvik seems to have solved all of our issues that we've been experiencing."</p><span class="name">Mette Kjær</span><span class="stars">★★★★★</span></div>
<div class="abs tcard" style="left:784px"><span class="quote">“</span><p>"I was very impressed with the package and services I received from Nordvik. The guys over there we really able to help me</p><span class="name">Lars Holmberg</span><span class="stars">★★★★★</span></div>
<div class="photo avatar" role="img" aria-label="Client portrait" style="left:126px;background:linear-gradient(135deg,#f2b640,#8a5a3c)"></div>
<div class="photo avatar" role="img" aria-label="Client portrait" style="left:472px;background:linear-gradient(135deg,#9aa6e0,#5b4a6e)"></div>
<div class="photo avatar" role="img" aria-label="Client portrait" style="left:817px;background:linear-gradient(135deg,#f06a4a,#b73a2a)"></div>

<div class="abs partner" style="left:187px"><i></i>Halvrik</div>
<div class="abs partner" style="left:357px"><i></i>Tenbury</div>
<div class="abs partner" style="left:527px"><i></i>Lumora</div>
<div class="abs partner" style="left:697px"><i></i>Vestra</div>
<div class="abs partner" style="left:867px"><i></i>Oakmere</div>

<!-- footer -->
<footer class="abs footer">
  <div class="fcol" style="left:88px"><h4>Online courses</h4><ul><li>Management</li><li>Office productivity suite</li><li>Online marketing</li><li>Performance &amp; Well-being</li><li>GDPR</li><li>Sales</li><li>Anti-corruption</li><li>Upcoming courses</li></ul></div>
  <div class="fcol" style="left:330px"><h4>Quick Links</h4><ul><li>Business</li><li>Prices</li><li>Customers</li><li>How an online course</li><li>Contact us</li><li>Vacancies (we hire!)</li></ul></div>
  <div class="fcol" style="left:537px"><h4>Need Help?</h4><ul><li>Try for free</li><li>Customer service</li><li>Membership conditions</li><li>Cookie and privacy policy</li></ul></div>
  <div class="fcol" style="left:750px"><h4>Contact Us</h4>
    <div class="contact"><svg width="11" height="11"><path d="M2 1h3l1 3-2 1a7 7 0 0 0 3 3l1-2 3 1v3A9 9 0 0 1 2 1z" fill="var(--green)"/></svg><b>PHONE*</b>+45 31 22 48 90</div>
    <div class="contact"><svg width="12" height="10"><rect x="0.5" y="0.5" width="11" height="8" fill="none" stroke="var(--green)"/><path d="M1 1l5 4 5-4" fill="none" stroke="var(--green)"/></svg><b>EMAIL*</b>hello@deskwizard.dk</div>
    <div class="contact"><svg width="10" height="13"><path d="M5 12S1 7 1 5a4 4 0 0 1 8 0c0 2-4 7-4 7z" fill="var(--green)"/></svg><b>LOCATION*</b>Some address line<br>goes here city name</div>
  </div>
  <div class="abs" style="left:88px;top:379px;width:1024px;height:1px;background:#2c3445"></div>
  <div class="abs" style="left:0;width:1200px;top:408px;text-align:center;font-size:10px;font-weight:600;color:#fff">© 2022 DESKWIZARD ALL RIGHTS RESERVED</div>
</footer>
<div class="abs social" style="left:946px"><i></i></div>
<div class="abs social" style="left:989px"><i></i></div>
<div class="abs social" style="left:1032px"><i></i></div>
<div class="abs social" style="left:1075px"><i></i></div>
<div class="abs round" style="left:1137px;top:4735px;width:40px;height:40px;background:var(--green);display:flex;align-items:center;justify-content:center"><svg width="10" height="7"><path d="M1 6l4-4 4 4" stroke="#fff" fill="none" stroke-width="1.6"/></svg></div>

</body>
</html>
```